Business Card Design Project

we need a business card design for our company: www.plomvik.ch
It's important to include our already existing logo (see website)

```html
<!DOCTYPE html>
<html lang="en">
<head>
<meta charset="utf-8">
<title>Plomvik AG – Business Card</title>
<link rel="stylesheet" href="https://fonts.googleapis.com/css2?family=Arimo:wght@400;700&display=swap">
<style>
  :root {
    --stage: #3a3b3d;
    --card-white: #ffffff;
    --brand-light: #7aaadc;
    --brand-blue: #1a73c4;
    --brand-deep: #1a5fa8;
    --label-blue: #7aa6d6;
    --on-blue: #ffffff;
  }
  * { box-sizing: border-box; margin: 0; padding: 0; }
  html, body {
    width: 1200px; height: 534px; overflow: hidden;
    background: var(--stage);
    font-family: "Arimo", Arial, sans-serif;
  }
  .stage { position: relative; width: 1200px; height: 534px; }
  .card {
    position: absolute; top: 120px;
    width: 512px; height: 291px;
    border-radius: 16px; overflow: hidden;
  }
  .card--front { left: 69px; background: var(--card-white); }
  .card--back { left: 621px; background: var(--brand-light); }
  .card__waves { position: absolute; inset: 0; }
  .wordmark {
    position: absolute; font-weight: 400; line-height: 1;
    letter-spacing: -0.5px;
  }
  .card--front .wordmark { left: 34px; top: 36px; font-size: 50px; color: var(--brand-blue); }
  .card--back .wordmark { left: 83px; top: 102px; font-size: 84px; color: var(--on-blue); }
  .details { position: absolute; left: 53px; top: 109px; color: var(--brand-deep); }
  .details__company { font-size: 18px; color: var(--brand-blue); margin-bottom: 8px; }
  .details__address { font-size: 13px; line-height: 13px; margin-bottom: 8px; }
  .contact { list-style: none; line-height: 12px; }
  .contact__label { font-size: 9px; color: var(--label-blue); }
  .contact__sep { font-size: 9px; color: var(--label-blue); margin: 0 2px; }
  .contact__value { font-size: 11.5px; }
  .back__url {
    position: absolute; left: 227px; top: 176px;
    font-size: 15px; font-weight: 700; color: var(--brand-deep);
  }
</style>
</head>
<body>
<main class="stage">
  <section class="card card--front" aria-label="Card front">
    <svg class="card__waves" width="512" height="291" viewBox="0 0 512 291" aria-hidden="true">
      <path d="M0,246 Q170,250 356,234 Q290,262 238,291 L0,291 Z" fill="var(--brand-blue)"/>
      <path d="M512,70 Q480,235 252,291 L512,291 Z" fill="var(--brand-light)"/>
    </svg>
    <div class="wordmark">Plomvik</div>
    <div class="details">
      <p class="details__company">Plomvik AG</p>
      <p class="details__address">Lindenweg 12<br>8004 Zürich</p>
      <ul class="contact">
        <li><span class="contact__label">Telephone</span><span class="contact__sep">|</span><span class="contact__value">+41 44 000 12 34</span></li>
        <li><span class="contact__label">Email</span><span class="contact__sep">|</span><span class="contact__value">info@plomvik.ch</span></li>
        <li><span class="contact__label">Skype</span><span class="contact__sep">|</span><span class="contact__value">plomvik.ch</span></li>
        <li><span class="contact__label">Website</span><span class="contact__sep">|</span><span class="contact__value">www.plomvik.ch</span></li>
      </ul>
    </div>
  </section>
  <section class="card card--back" aria-label="Card back">
    <div class="wordmark">Plomvik</div>
    <p class="back__url">www.plomvik.ch</p>
  </section>
</main>
</body>
</html>
```